Web Page Re-designed

Looking to have this portion of a webpage on my site re-designed to look a little more clean and professional, the layout and organization of the data can be changed for example the location name does not have to keep repeating itself its schedule for a sports league

Reason: Still looking fo the right design

It Professional

```html
<!DOCTYPE html>
<html lang="en">
<head>
<meta charset="utf-8">
<title>Rinkline Sports – Wednesday Co-ed Ball Hockey Schedule</title>
<link href="https://fonts.googleapis.com/css2?family=Didact+Gothic&family=Oswald:wght@400;500&display=swap" rel="stylesheet">
<style>
:root{
  --page:#2b2b2b;
  --panel:#f9f9f7;
  --ink:#2a2a2a;
  --green:#7fae3c;
  --green-dark:#5b8526;
  --green-ink:#2f4d12;
  --footer:#86b03e;
  --tab:#4a4a4a;
  --header-yellow:#fde57a;
  --rule:#c9b96a;
  --divider:#b8b8b8;
  --jersey-gold:#e1b43a;
  --jersey-red:#c9141a;
  --banner-blue:#1b4e8c;
  --white:#ffffff;
}
*{box-sizing:border-box;margin:0;padding:0}
html,body{width:1161px;height:1200px;overflow:hidden}
body{background:var(--page);font-family:"Didact Gothic",sans-serif;color:var(--ink);position:relative}
.abs{position:absolute}
.brand{left:88px;top:52px;font-family:"Didact Gothic",sans-serif;font-size:30px;color:#e9f0c8;letter-spacing:1px}
.side-nav{left:79px;top:122px;width:206px;list-style:none}
.side-nav li{height:26px;margin-bottom:7px;background:var(--green);border:1px solid var(--green-dark);color:var(--green-ink);font-size:15px;text-align:center;line-height:26px}
.main-nav{left:334px;top:58px;width:727px;display:flex;justify-content:space-between;list-style:none}
.main-nav li{font-family:"Oswald",sans-serif;font-weight:500;font-size:16px;color:var(--white);border-top:1px solid #9a9a9a;padding-top:9px;letter-spacing:.3px}
.main-nav li.active{border-top:3px solid var(--white);padding-top:7px}
.banner{left:334px;top:132px;width:729px;height:142px;background:linear-gradient(90deg,#b3322d,#d9c3b0 30%,#e6e0d6 55%,#b9231f 80%,#ddd 100%)}
.social{left:535px;top:246px;width:349px;height:28px;background:var(--banner-blue);border-radius:8px 8px 0 0;color:var(--white);font-size:17px;letter-spacing:1.5px;display:flex;align-items:center;justify-content:center;gap:8px}
.social .dot{width:22px;height:22px;border-radius:50%;background:var(--white)}
.title-bar{left:334px;top:281px;width:729px;height:29px;background:var(--white);border-radius:0 0 6px 6px;display:flex;align-items:center;padding:0 24px 0 23px;justify-content:space-between}
.title-bar h1{font-weight:400;font-size:15px;font-variant:small-caps;text-decoration:underline;letter-spacing:.3px}
.season{display:flex;align-items:center;gap:9px;font-variant:small-caps;font-size:15px}
.season .select{display:flex;align-items:center;width:109px;height:20px;background:#2f2f2f;color:var(--white);font-size:14px;padding-left:4px;justify-content:space-between}
.season .select span.arrow{width:20px;height:20px;background:#f0cd2c;display:flex;align-items:center;justify-content:center}
.tab{top:350px;height:29px;background:var(--tab);border-radius:8px 8px 0 0;color:var(--white);font-size:16px;display:flex;align-items:center;justify-content:center;position:absolute}
.tab svg{position:absolute;right:13px;top:8px}
.panel{left:75px;top:379px;width:985px;height:723px;background:var(--panel)}
.day{position:absolute;left:6px;width:731px}
.day-label{width:151px;height:25px;border:1px solid #8c8c62;background:var(--white);font-size:14px;letter-spacing:1px;padding:5px 0 0 5px;text-transform:uppercase}
.table{margin-top:5px;border:1px solid var(--rule);background:var(--panel);height:139px;position:relative;margin-left:-1px}
.thead{height:22px;background:var(--header-yellow);border-bottom:1px solid var(--rule);position:relative;font-size:15px;letter-spacing:.5px}
.thead span{position:absolute;top:2px;transform:translateX(-50%)}
.row{height:34px;position:relative;font-size:15px;letter-spacing:.8px}
.row + .row{border-top:1px solid #d5d5d5}
.row:first-of-type{margin-top:2px}
.row span{position:absolute;top:9px}
.row i{position:absolute;top:5px;width:1px;height:25px;background:var(--divider)}
.row svg{position:absolute;top:6px}
.row.first{border-top:none}
.side{position:absolute;left:764px;width:211px;border:1px solid #9b9b9b;border-top:none;background:var(--panel)}
.side h2{font-weight:400;font-size:15px;color:var(--white);background:var(--tab);height:28px;line-height:30px;padding-left:27px;border-radius:7px 7px 0 0;margin:0 -1px}
.side ul{list-style:none;padding:3px 0 0 43px;font-size:14.5px;line-height:20.5px;letter-spacing:.3px}
.login{position:absolute;left:764px;top:476px;width:211px;height:27px;background:var(--tab);border-radius:7px 7px 0 0;color:var(--white);font-size:15px;padding:4px 0 0 32px}
.footer{left:0;top:1121px;width:1161px;height:79px;background:var(--footer);color:var(--white);font-size:15px;letter-spacing:.5px;text-align:center;padding-top:26px}
</style>
</head>
<body>
<svg width="0" height="0" style="position:absolute">
  <defs>
    <symbol id="jersey" viewBox="0 0 22 22"><path d="M7 1h8l6 4-3 5-2-1v12H6V9L4 10 1 5z"/></symbol>
  </defs>
</svg>

<div class="abs brand">Rinkline Sports</div>

<ul class="abs side-nav">
  <li>HOME</li><li>ABOUT US</li><li>FAQS</li><li>CONTACT US</li><li>JOBS</li><li>SPONSORS</li>
</ul>

<ul class="abs main-nav">
  <li>LEAGUES</li><li class="active">SCHEDULES &amp; MORE</li><li>REGISTER</li><li>PAY</li><li>FORUM</li><li>TOURNAMENTS</li>
</ul>

<div class="abs banner" role="img" aria-label="Row of league player portraits"></div>
<div class="abs social"><span class="dot"></span>Find us on Linkora</div>

<div class="abs title-bar">
  <h1>Wednesday Co-ed Ball Hockey Schedule</h1>
  <div class="season">Season <div class="select">FALL 2013<span class="arrow"><svg width="12" height="11"><path d="M0 0h12L6 11z" fill="#222"/></svg></span></div></div>
</div>

<div class="tab" style="left:75px;width:348px">- SELECT TEAM -<svg width="13" height="12"><path d="M0 0h13L6.5 12z" fill="#fff"/></svg></div>
<div class="tab" style="left:462px;width:350px">REGULAR SEASON/EXHIBITION<svg width="13" height="12"><path d="M0 0h13L6.5 12z" fill="#fff"/></svg></div>

<div class="abs panel">

  <!-- Day blocks -->
  <section class="day" style="top:5px">
    <div class="day-label">Wednesday Oct 6th</div>
    <div class="table">
      <div class="thead"><span style="left:66px">TIME</span><span style="left:163px">HOME</span><span style="left:359px">AWAY</span><span style="left:548px">LOCATION</span><span style="left:663px">STICK</span></div>
      <div class="row first"><span style="left:11px">RS</span><span style="left:42px">8:00pm</span><i style="left:116px"></i><span style="left:144px">Blue Lines</span><svg style="left:239px" width="22" height="22" fill="var(--jersey-gold)"><use href="#jersey"/></svg><span style="left:265px">vs.</span><i style="left:299px"></i><span style="left:311px">Top Shelf</span><i style="left:427px"></i><svg style="left:440px" width="22" height="22" fill="var(--jersey-red)"><use href="#jersey"/></svg><i style="left:475px"></i><span style="left:491px">Northgate Arena</span><i style="left:615px"></i></div>
      <div class="row"><span style="left:11px">RS</span><span style="left:42px">8:00pm</span><i style="left:116px"></i><span style="left:144px">Blue Lines</span><svg style="left:239px" width="22" height="22" fill="var(--jersey-gold)"><use href="#jersey"/></svg><span style="left:265px">vs.</span><i style="left:299px"></i><span style="left:311px">Top Shelf</span><i style="left:427px"></i><svg style="left:440px" width="22" height="22" fill="var(--jersey-red)"><use href="#jersey"/></svg><i style="left:475px"></i><span style="left:491px">Northgate Arena</span><i style="left:615px"></i></div>
      <div class="row"><span style="left:11px">RS</span><span style="left:42px">8:00pm</span><i style="left:116px"></i><span style="left:144px">Blue Lines</span><svg style="left:239px" width="22" height="22" fill="var(--jersey-gold)"><use href="#jersey"/></svg><span style="left:265px">vs.</span><i style="left:299px"></i><span style="left:311px">Top Shelf</span><i style="left:427px"></i><svg style="left:440px" width="22" height="22" fill="var(--jersey-red)"><use href="#jersey"/></svg><i style="left:475px"></i><span style="left:491px">Northgate Arena</span><i style="left:615px"></i></div>
    </div>
  </section>

  <section class="day" style="top:180px">
    <div class="day-label">Wednesday Oct 6th</div>
    <div class="table">
      <div class="thead"><span style="left:66px">TIME</span><span style="left:163px">HOME</span><span style="left:359px">AWAY</span><span style="left:548px">LOCATION</span><span style="left:663px">STICK</span></div>
      <div class="row first"><span style="left:11px">RS</span><span style="left:42px">8:00pm</span><i style="left:116px"></i><span style="left:144px">Blue Lines</span><svg style="left:239px" width="22" height="22" fill="var(--jersey-gold)"><use href="#jersey"/></svg><span style="left:265px">vs.</span><i style="left:299px"></i><span style="left:311px">Top Shelf</span><i style="left:427px"></i><svg style="left:440px" width="22" height="22" fill="var(--jersey-red)"><use href="#jersey"/></svg><i style="left:475px"></i><span style="left:491px">Northgate Arena</span><i style="left:615px"></i></div>
      <div class="row"><span style="left:11px">RS</span><span style="left:42px">8:00pm</span><i style="left:116px"></i><span style="left:144px">Blue Lines</span><svg style="left:239px" width="22" height="22" fill="var(--jersey-gold)"><use href="#jersey"/></svg><span style="left:265px">vs.</span><i style="left:299px"></i><span style="left:311px">Top Shelf</span><i style="left:427px"></i><svg style="left:440px" width="22" height="22" fill="var(--jersey-red)"><use href="#jersey"/></svg><i style="left:475px"></i><span style="left:491px">Northgate Arena</span><i style="left:615px"></i></div>
      <div class="row"><span style="left:11px">RS</span><span style="left:42px">8:00pm</span><i style="left:116px"></i><span style="left:144px">Blue Lines</span><svg style="left:239px" width="22" height="22" fill="var(--jersey-gold)"><use href="#jersey"/></svg><span style="left:265px">vs.</span><i style="left:299px"></i><span style="left:311px">Top Shelf</span><i style="left:427px"></i><svg style="left:440px" width="22" height="22" fill="var(--jersey-red)"><use href="#jersey"/></svg><i style="left:475px"></i><span style="left:491px">Northgate Arena</span><i style="left:615px"></i></div>
    </div>
  </section>

  <section class="day" style="top:354px">
    <div class="day-label">Wednesday Oct 6th</div>
    <div class="table">
      <div class="thead"><span style="left:66px">TIME</span><span style="left:163px">HOME</span><span style="left:359px">AWAY</span><span style="left:548px">LOCATION</span><span style="left:663px">STICK</span></div>
      <div class="row first"><span style="left:11px">RS</span><span style="left:42px">8:00pm</span><i style="left:116px"></i><span style="left:144px">Blue Lines</span><svg style="left:239px" width="22" height="22" fill="var(--jersey-gold)"><use href="#jersey"/></svg><span style="left:265px">vs.</span><i style="left:299px"></i><span style="left:311px">Top Shelf</span><i style="left:427px"></i><svg style="left:440px" width="22" height="22" fill="var(--jersey-red)"><use href="#jersey"/></svg><i style="left:475px"></i><span style="left:491px">Northgate Arena</span><i style="left:615px"></i></div>
      <div class="row"><span style="left:11px">RS</span><span style="left:42px">8:00pm</span><i style="left:116px"></i><span style="left:144px">Blue Lines</span><svg style="left:239px" width="22" height="22" fill="var(--jersey-gold)"><use href="#jersey"/></svg><span style="left:265px">vs.</span><i style="left:299px"></i><span style="left:311px">Top Shelf</span><i style="left:427px"></i><svg style="left:440px" width="22" height="22" fill="var(--jersey-red)"><use href="#jersey"/></svg><i style="left:475px"></i><span style="left:491px">Northgate Arena</span><i style="left:615px"></i></div>
      <div class="row"><span style="left:11px">RS</span><span style="left:42px">8:00pm</span><i style="left:116px"></i><span style="left:144px">Blue Lines</span><svg style="left:239px" width="22" height="22" fill="var(--jersey-gold)"><use href="#jersey"/></svg><span style="left:265px">vs.</span><i style="left:299px"></i><span style="left:311px">Top Shelf</span><i style="left:427px"></i><svg style="left:440px" width="22" height="22" fill="var(--jersey-red)"><use href="#jersey"/></svg><i style="left:475px"></i><span style="left:491px">Northgate Arena</span><i style="left:615px"></i></div>
    </div>
  </section>

  <section class="day" style="top:529px">
    <div class="day-label">Wednesday Oct 6th</div>
    <div class="table">
      <div class="thead"><span style="left:66px">TIME</span><span style="left:163px">HOME</span><span style="left:359px">AWAY</span><span style="left:548px">LOCATION</span><span style="left:663px">STICK</span></div>
      <div class="row first"><span style="left:11px">RS</span><span style="left:42px">8:00pm</span><i style="left:116px"></i><span style="left:144px">Blue Lines</span><svg style="left:239px" width="22" height="22" fill="var(--jersey-gold)"><use href="#jersey"/></svg><span style="left:265px">vs.</span><i style="left:299px"></i><span style="left:311px">Top Shelf</span><i style="left:427px"></i><svg style="left:440px" width="22" height="22" fill="var(--jersey-red)"><use href="#jersey"/></svg><i style="left:475px"></i><span style="left:491px">Northgate Arena</span><i style="left:615px"></i></div>
      <div class="row"><span style="left:11px">RS</span><span style="left:42px">8:00pm</span><i style="left:116px"></i><span style="left:144px">Blue Lines</span><svg style="left:239px" width="22" height="22" fill="var(--jersey-gold)"><use href="#jersey"/></svg><span style="left:265px">vs.</span><i style="left:299px"></i><span style="left:311px">Top Shelf</span><i style="left:427px"></i><svg style="left:440px" width="22" height="22" fill="var(--jersey-red)"><use href="#jersey"/></svg><i style="left:475px"></i><span style="left:491px">Northgate Arena</span><i style="left:615px"></i></div>
      <div class="row"><span style="left:11px">RS</span><span style="left:42px">8:00pm</span><i style="left:116px"></i><span style="left:144px">Blue Lines</span><svg style="left:239px" width="22" height="22" fill="var(--jersey-gold)"><use href="#jersey"/></svg><span style="left:265px">vs.</span><i style="left:299px"></i><span style="left:311px">Top Shelf</span><i style="left:427px"></i><svg style="left:440px" width="22" height="22" fill="var(--jersey-red)"><use href="#jersey"/></svg><i style="left:475px"></i><span style="left:491px">Northgate Arena</span><i style="left:615px"></i></div>
    </div>
  </section>

  <!-- Sidebar -->
  <nav class="side" style="top:33px;height:138px">
    <h2>SCHEDULES</h2>
    <ul><li>Division A</li><li>Division B</li><li>Division C</li><li>All Divisions</li><li>Playoffs</li></ul>
  </nav>
  <nav class="side" style="top:188px;height:117px">
    <h2>START MENU</h2>
    <ul style="padding-left:38px"><li>Game Rules</li><li>Scoreboard</li><li>Standings</li><li>Leaders</li></ul>
  </nav>
  <nav class="side" style="top:323px;height:137px">
    <h2>QUICK LINKS</h2>
    <ul><li>Rules</li><li>Teams</li><li>News</li><li>Free Agents</li><li>Champ T-Shirt Request</li></ul>
  </nav>
  <div class="login">LOGIN <svg width="10" height="10" style="margin-left:26px"><path d="M0 0l10 5-10 5 3-5z" fill="#fff"/></svg></div>
</div>

<footer class="abs footer">© 2011-2012, SPORTS. ALL RIGHTS RESERVED, Data Feed by leaguefeed.net</footer>
</body>
</html>
```